Two Day Training Event includes a Dinner/Bowling Party at Larkspur in Troy, MI

I would like a postcard to attract Insurance Agents to an QWT meeting calling it a summit or something like that. Just something to mail to insurance agents telling them about our upcoming event with over 20 carriers. An opportunity to certify face to face with MAPD carriers and see what 2020 has to offer. Prior to OEP OPen Enrollment and AEP Annual Election period we have a number of meetings. Carriers want to come especially if we can get a number of agents. We are going to go to Larkspur a fun bowling alley for dinner, drinks and bowling to network and talk about the upcoming year.

Target Market(s)

Existing and new insurance agents

Industry/Entity Type

Insurance Broker

Contact Information for Business Card

Looking for a new card design I sent my LOGO and can upload my existing card.

Font styles to use
Serif

Colors

Designer to choose colors to be used in the design.

Requirements
Must have
• Dates Sept 16 and 17th
• location Harrowgate Conference Hall in Troy MI
• times
Nice to have
• It would be nice to see a fun design.

```html
<!DOCTYPE html>
<html lang="en">
<head>
<meta charset="utf-8">
<title>Let's meet and bowl</title>
<link rel="stylesheet" href="https://fonts.googleapis.com/css2?family=Arimo:wght@400;700&family=Questrial&display=swap">
<style>
  :root {
    --night: #07070c;
    --panel: rgba(0, 0, 48, 0.82);
    --panel-solid: rgba(0, 0, 40, 0.9);
    --ink: #ffffff;
    --ink-soft: #dfe3ff;
  }
  html, body {
    margin: 0;
    padding: 0;
    width: 800px;
    height: 1200px;
    overflow: hidden;
    background: var(--night);
  }
  .card {
    position: relative;
    width: 800px;
    height: 1200px;
    overflow: hidden;
    color: var(--ink);
  }
  .scene {
    position: absolute;
    inset: 0;
    background:
      radial-gradient(ellipse 240px 340px at 90px 470px, rgba(40, 60, 255, 0.8), transparent 70%),
      radial-gradient(ellipse 150px 260px at 720px 440px, rgba(215, 205, 195, 0.45), transparent 70%),
      radial-gradient(ellipse 120px 200px at 700px 620px, rgba(160, 120, 70, 0.35), transparent 70%),
      linear-gradient(180deg, #050507 0%, #0d0d14 30%, #1a1616 55%, #4a3320 76%, #2a3a8a 100%);
  }
  .headline {
    position: absolute;
    top: 22px;
    left: 0;
    width: 800px;
    margin: 0;
    text-align: center;
    font-family: "Arimo", Arial, sans-serif;
    font-weight: 700;
    font-size: 52px;
    letter-spacing: 4px;
    line-height: 1.2;
  }
  .announcement {
    position: absolute;
    left: 0;
    top: 136px;
    width: 584px;
    height: 592px;
    box-sizing: border-box;
    padding: 36px 8px 0 6px;
    background: var(--panel);
    font-family: "Questrial", "Century Gothic", sans-serif;
    font-style: italic;
    font-size: 35px;
    letter-spacing: 0.3px;
    line-height: 48px;
    white-space: nowrap;
  }
  .announcement p {
    margin: 0 0 56px;
  }
  .announcement .indent {
    padding-left: 142px;
  }
  .dates {
    position: absolute;
    left: 109px;
    top: 752px;
    width: 583px;
    height: 132px;
    box-sizing: border-box;
    padding-top: 20px;
    background: var(--panel-solid);
    text-align: center;
    font-family: "Arimo", Arial, sans-serif;
    font-weight: 700;
  }
  .dates .days {
    display: block;
    font-size: 47px;
    letter-spacing: 3px;
    line-height: 56px;
  }
  .dates .venue {
    display: block;
    margin-top: 8px;
    font-weight: 400;
    font-size: 20px;
    line-height: 26px;
    color: var(--ink-soft);
  }
  .agent {
    position: absolute;
    left: 109px;
    top: 919px;
    width: 583px;
    height: 177px;
    box-sizing: border-box;
    padding: 24px 0 0 38px;
    background: var(--panel-solid);
    font-family: "Arimo", Arial, sans-serif;
    font-weight: 700;
    font-size: 27px;
    line-height: 40px;
  }
  .agent span {
    display: block;
  }
  .agent .name, .agent .specialty {
    padding-left: 10px;
  }
</style>
</head>
<body>
  <div class="card">
    <div class="scene" role="img" aria-label="Photo of a bowling alley lane with a ball striking white pins, blue glowing lights on the left"></div>

    <h1 class="headline">Let‘s meet and bowl...</h1>

    <div class="announcement">
      <p>This is to announce that we<br>are planning a fun meetup<br>for our agents to network and<br>meet face to face with the<br>MAPD carriers.</p>
      <p><span class="indent">let us &nbsp; go to Larkspur a</span><br>fun bowling alley for dinner,<br>drinks and bowling to<br>network and talk about the<br>upcoming year</p>
    </div>

    <p class="dates" style="margin:0">
      <span class="days">Sept 16 and 17th</span>
      <span class="venue">9:00 am – 4:00 pm · Harrowgate Conference Hall, Troy MI</span>
    </p>

    <div class="agent">
      <span class="name">Dale Moravec</span>
      <span class="title">Licensed Health and Life Agent</span>
      <span class="specialty">Health and Medicare Specialist</span>
    </div>
  </div>
</body>
</html>
```